Business Card Design Project - IT Company

Kestrafield Information Technology Solutions
We are an Information Technology Company. We provide computer services to commercial companies. We would like a new card full color front and back with bleeding edge.
We have a logo that you can use or if you want to come up with a new logo that is fine too.
Our colors are mostly Maroon and black but be creative.
Sample Information
Brent R Okafor
4812 W Saguaro Ridge Drive
Suite 600
Phoenix, AZ 85016
O: 602.914.2037
C: 602.468.1290
24/7: 888.914.2037
bokafor@kestrafield.example
www.kestrafield.example
Target Market(s)
Business of all sizes
Industry/Entity Type
Computer
Requirements
Must have
- Bleeding edge
full color on both sides

```html
<!DOCTYPE html>
<html lang="en">
<head>
<meta charset="utf-8">
<title>Kestrafield Business Card</title>
<link rel="stylesheet" href="https://fonts.googleapis.com/css2?family=Open+Sans:wght@400;700&family=Tinos&display=swap">
<style>
  :root {
    --card-black: #000000;
    --maroon-light: #d8213a;
    --maroon-dark: #a31a26;
    --edge-white: #ffffff;
    --brand-grey: #5c5d5f;
    --tagline-grey: #8e8e8e;
    --text-grey: #8a8a8a;
    --name-grey: #909090;
  }
  html, body {
    margin: 0;
    padding: 0;
    width: 1200px;
    height: 695px;
    overflow: hidden;
    background: var(--card-black);
  }
  .card {
    position: relative;
    width: 1200px;
    height: 695px;
    background: var(--card-black);
    overflow: hidden;
    font-family: "Open Sans", Arial, sans-serif;
  }
  .card-frame {
    position: absolute;
    inset: 0;
  }
  .brand {
    position: absolute;
    left: 12px;
    right: 0;
    top: 282px;
    text-align: center;
    margin: 0;
    font-family: "Open Sans", Arial, sans-serif;
    font-weight: 700;
    font-size: 82px;
    letter-spacing: 12px;
    line-height: 1;
    color: var(--brand-grey);
  }
  .tagline {
    position: absolute;
    left: 0;
    right: 0;
    top: 404px;
    text-align: center;
    margin: 0;
    font-family: "Tinos", "Times New Roman", serif;
    font-size: 42px;
    line-height: 1;
    color: var(--tagline-grey);
  }
  .company-details {
    position: absolute;
    left: 128px;
    top: 508px;
    margin: 0;
    font-size: 23px;
    line-height: 32px;
    color: var(--text-grey);
    font-style: normal;
  }
  .contact-person {
    position: absolute;
    right: 129px;
    top: 500px;
    margin: 0;
    text-align: right;
    font-size: 23px;
    line-height: 32px;
    color: var(--text-grey);
    font-style: normal;
  }
  .contact-name {
    display: block;
    font-size: 29px;
    font-weight: 700;
    line-height: 40px;
    color: var(--name-grey);
  }
  .line { display: block; white-space: nowrap; }
</style>
</head>
<body>
<main class="card">
  <svg class="card-frame" width="1200" height="695" viewBox="0 0 1200 695" aria-hidden="true">
    <defs>
      <linearGradient id="panel-red" x1="0" y1="0" x2="0" y2="1">
        <stop offset="0" stop-color="var(--maroon-light)"/>
        <stop offset="1" stop-color="var(--maroon-dark)"/>
      </linearGradient>
      <filter id="edge-glow" x="-50%" y="-10%" width="200%" height="120%">
        <feGaussianBlur stdDeviation="14"/>
      </filter>
    </defs>
    <path d="M61 -5 C128 200 128 495 61 700" fill="none" stroke="#ffffff" stroke-opacity="0.35" stroke-width="14" filter="url(#edge-glow)"/>
    <path d="M1139 -5 C1072 200 1072 495 1139 700" fill="none" stroke="#ffffff" stroke-opacity="0.35" stroke-width="14" filter="url(#edge-glow)"/>
    <path class="side-panel" d="M0 0 H61 C128 200 128 495 61 695 H0 Z" fill="url(#panel-red)"/>
    <path class="side-panel" d="M1200 0 H1139 C1072 200 1072 495 1139 695 H1200 Z" fill="url(#panel-red)"/>
    <path d="M61 0 C128 200 128 495 61 695" fill="none" stroke="var(--edge-white)" stroke-width="2.5"/>
    <path d="M1139 0 C1072 200 1072 495 1139 695" fill="none" stroke="var(--edge-white)" stroke-width="2.5"/>
  </svg>

  <h1 class="brand">KESTRAFIELD</h1>
  <p class="tagline">Information Technology Solutions</p>

  <address class="company-details">
    <span class="line">4812 W Saguaro Ridge Drive</span>
    <span class="line">Suite 410&nbsp; Phoenix, AZ 85021</span>
    <span class="line">24/7: 888.914.2037</span>
    <span class="line">www.kestrafield.example</span>
  </address>

  <address class="contact-person">
    <span class="contact-name">BRENT R OKAFOR</span>
    <span class="line">bokafor@kestrafield.example</span>
    <span class="line">C: 602.468.1290</span>
    <span class="line">O: 602.914.2037</span>
  </address>
</main>
</body>
</html>
```